Sun Jubilee - Concert Poster

We need a poster for a concert involving 3 bands. Marmaduke, Auntie's Gumbo and Velveteen Ray. The event is called the Sun Jubilee. The poster will be a take away. We plan to print some to give out and some for advertising. Should be something people will want to put up on a wall. The poster should have a psychedelic "flavor", colorful.
Info. that needs to be on the poster: Sun Jubilee - Band Names - Pelham Brook's Music Hall - 4182 Route 17, Felton CA - $10 advance Tix - $12 at Door - for tickets www.pelhambrookmusic. - 21 and Over - March 21 2015 - Doors open at 7:00.

Industry/Entity Type

Event

```html
<!DOCTYPE html>
<html lang="en">
<head>
<meta charset="utf-8">
<title>Sun Jubilee – Concert Poster</title>
<link rel="stylesheet" href="https://fonts.googleapis.com/css2?family=Cousine:wght@400;700&family=Stardos+Stencil:wght@700&display=swap">
<style>
  :root {
    --backdrop: #e8e4de;
    --heart-red: #f20d0d;
    --tile-white: #fbfbf4;
    --ink: #1c1420;
    --ink-soft: #2b1d2e;
    --note-pink: #e81ad8;
    --psy-green: #7cf03a;
    --psy-yellow: #f4ee52;
    --psy-pink: #f36fb0;
    --psy-orange: #f47a3a;
    --petal-yellow: #f7f25a;
    --petal-orange: #f6b870;
    --centre-blue: #1aa6d6;
    --centre-green: #14c51e;
  }
  * { box-sizing: border-box; margin: 0; padding: 0; }
  html, body {
    width: 1200px; height: 900px; overflow: hidden;
    background: var(--backdrop);
  }
  .poster {
    position: absolute; left: 266px; top: 20px;
    width: 668px; height: 860px; overflow: hidden;
    font-family: "Cousine", monospace;
    background:
      radial-gradient(circle at 8% 10%, var(--psy-green) 0, transparent 22%),
      radial-gradient(circle at 84% 5%, var(--psy-green) 0, transparent 18%),
      radial-gradient(circle at 102% 0%, var(--psy-pink) 0, transparent 16%),
      radial-gradient(circle at 88% 40%, var(--psy-green) 0, transparent 14%),
      radial-gradient(circle at 0% 45%, var(--psy-pink) 0, transparent 24%),
      radial-gradient(circle at 50% 30%, var(--psy-yellow) 0, transparent 55%),
      linear-gradient(180deg, #f6ce55 0%, #f4c84e 45%, #f48e4c 75%, #f2744a 100%);
  }
  .crowd-photo {
    position: absolute; left: 150px; top: 470px; width: 540px; height: 420px;
    background:
      radial-gradient(ellipse 30% 25% at 45% 22%, rgba(250,170,140,.85) 0, rgba(250,170,140,0) 100%),
      radial-gradient(ellipse 55% 45% at 60% 70%, rgba(178,30,26,.85) 0, rgba(220,60,40,.55) 55%, rgba(240,110,70,0) 100%),
      radial-gradient(ellipse 60% 55% at 50% 50%, rgba(245,110,80,.7) 0, rgba(245,110,80,0) 100%);
  }
  .artwork { position: absolute; inset: 0; }
  .pin {
    position: absolute; width: 8px; height: 8px; border-radius: 50%;
    background: var(--ink);
  }
  .title { position: absolute; inset: 0; }
  .tile {
    position: absolute; width: 52px; height: 66px;
    background: var(--tile-white);
    box-shadow: 0 1px 2px rgba(0,0,0,.25);
    font-family: "Stardos Stencil", sans-serif; font-weight: 700;
    font-size: 46px; line-height: 66px; text-align: center; color: var(--ink);
  }
  .band {
    position: absolute; left: 0; width: 100%; text-align: center;
    color: #fff; white-space: nowrap; font-weight: 400;
    text-shadow: -1.5px -1.5px 0 var(--ink), 1.5px -1.5px 0 var(--ink), -1.5px 1.5px 0 var(--ink), 1.5px 1.5px 0 var(--ink), 0 1.5px 0 var(--ink), 0 -1.5px 0 var(--ink), 1.5px 0 0 var(--ink), -1.5px 0 0 var(--ink);
  }
  .band--headliner { top: 232px; font-size: 98px; line-height: 100px; }
  .band--second { top: 308px; font-size: 56px; line-height: 60px; }
  .band--third { top: 357px; font-size: 70px; line-height: 80px; }
  .tickets {
    position: absolute; left: 406px; width: 250px; top: 480px;
    text-align: center; font-size: 14px; line-height: 17.5px; color: var(--ink);
  }
  .venue {
    position: absolute; left: 40px; width: 250px; top: 657px;
    text-align: center; font-size: 13px; line-height: 16px; color: var(--ink-soft);
    font-style: normal;
  }
  .details {
    position: absolute; left: 17px; bottom: 12px;
    font-size: 26px; line-height: 26px; color: var(--ink-soft);
  }
</style>
</head>
<body>
<main class="poster">
  <div class="crowd-photo" role="img" aria-label="Photo of a concert crowd with raised hands under warm red stage light"></div>

  <svg class="artwork" width="668" height="860" viewBox="0 0 668 860">
    <defs>
      <radialGradient id="heartGlow" cx="335" cy="460" r="100" gradientUnits="userSpaceOnUse">
        <stop offset="0" stop-color="#fff"/>
        <stop offset=".45" stop-color="#fff" stop-opacity=".85"/>
        <stop offset="1" stop-color="#fff" stop-opacity="0"/>
      </radialGradient>
      <radialGradient id="softRed" cx="50%" cy="50%" r="50%">
        <stop offset=".55" stop-color="#f20d0d"/>
        <stop offset="1" stop-color="#f20d0d" stop-opacity="0"/>
      </radialGradient>
      <radialGradient id="flowerYellow"><stop offset=".35" stop-color="var(--centre-blue)"/><stop offset=".4" stop-color="var(--petal-yellow)"/></radialGradient>
      <radialGradient id="flowerOrange"><stop offset=".35" stop-color="var(--centre-green)"/><stop offset=".4" stop-color="var(--petal-orange)"/></radialGradient>
    </defs>

    <ellipse cx="146" cy="688" rx="130" ry="82" fill="url(#softRed)"/>
    <path d="M146 766 C 90 725, 28 700, 30 660 C 32 625, 70 612, 100 622 C 120 630, 140 642, 146 652 C 152 642, 172 630, 192 622 C 222 612, 262 625, 262 660 C 264 700, 202 725, 146 766 Z" fill="var(--heart-red)" opacity=".9"/>

    <path d="M335 200 C 300 150, 230 160, 170 164 C 100 170, 62 215, 70 275 C 80 345, 200 425, 335 514 C 470 425, 590 345, 598 275 C 605 215, 568 170, 500 164 C 440 160, 370 150, 335 200 Z" fill="var(--heart-red)" stroke="#b30909" stroke-width="1"/>
    <path d="M335 200 C 300 150, 230 160, 170 164 C 100 170, 62 215, 70 275 C 80 345, 200 425, 335 514 C 470 425, 590 345, 598 275 C 605 215, 568 170, 500 164 C 440 160, 370 150, 335 200 Z" fill="url(#heartGlow)"/>

    <g class="note" fill="var(--note-pink)" stroke="#8a0f80" stroke-width="1">
      <ellipse cx="92" cy="590" rx="52" ry="30" transform="rotate(-18 92 590)"/>
      <rect x="130" y="456" width="14" height="130"/>
      <path d="M130 456 C 164 470, 200 500, 186 540 C 176 565, 166 585, 156 590 C 176 560, 176 520, 144 505 Z"/>
    </g>
    <g class="note" fill="var(--note-pink)" stroke="#8a0f80" stroke-width="1">
      <ellipse cx="555" cy="806" rx="50" ry="28" transform="rotate(-18 555 806)"/>
      <rect x="592" y="675" width="14" height="128"/>
      <path d="M592 675 C 626 690, 650 718, 640 752 C 634 772, 626 780, 618 785 C 630 760, 628 730, 606 720 Z"/>
    </g>

    <circle cx="340" cy="35" r="37" fill="url(#flowerYellow)" stroke="var(--ink)" stroke-width="1.5"/>
    <circle cx="335" cy="191" r="62" fill="url(#flowerOrange)" stroke="var(--ink)" stroke-width="1.5"/>
    <circle cx="30" cy="548" r="27" fill="url(#flowerOrange)" stroke="var(--ink)" stroke-width="1.5"/>
    <circle cx="322" cy="545" r="36" fill="url(#flowerYellow)" stroke="var(--ink)" stroke-width="1.5"/>
    <circle cx="506" cy="775" r="36" fill="url(#flowerYellow)" stroke="var(--ink)" stroke-width="1.5"/>
  </svg>

  <span class="pin" style="left:8px;top:8px"></span>
  <span class="pin" style="right:8px;top:8px"></span>
  <span class="pin" style="left:8px;bottom:8px"></span>
  <span class="pin" style="right:8px;bottom:8px"></span>

  <h1 class="title" aria-label="Sun Jubilee">
    <span class="tile" style="left:23px;top:98px;transform:rotate(-14.5deg)">S</span>
    <span class="tile" style="left:79px;top:85px;transform:rotate(-11.7deg)">U</span>
    <span class="tile" style="left:135px;top:75px;transform:rotate(-8.8deg)">N</span>
    <span class="tile" style="left:247px;top:63px;transform:rotate(-2.9deg)">J</span>
    <span class="tile" style="left:303px;top:62px">U</span>
    <span class="tile" style="left:359px;top:64px;transform:rotate(3.1deg)">B</span>
    <span class="tile" style="left:415px;top:68px;transform:rotate(6.1deg)">I</span>
    <span class="tile" style="left:471px;top:76px;transform:rotate(9deg)">L</span>
    <span class="tile" style="left:527px;top:86px;transform:rotate(11.9deg)">E</span>
    <span class="tile" style="left:583px;top:99px;transform:rotate(14.7deg)">E</span>
  </h1>

  <h2 class="band band--headliner">MARMADUKE</h2>
  <h2 class="band band--second">Auntie’s Gumbo</h2>
  <h2 class="band band--third">Velveteen Ray</h2>

  <p class="tickets">$10 Advanced Tickets<br>$12 On The Door<br>For Tickets visit:<br>www.pelhambrookmusic.info</p>

  <address class="venue">Pelham Brook’s Music Hall<br>4182 Route 17,<br>Felton CA</address>

  <p class="details">21 &amp; Over<br>March 21st 2015<br>Doors Open at 7.00pm</p>
</main>
</body>
</html>
```